依頼詳細
◆依頼するLP制作の概要
・ワイヤーフレームはこちらで製作済みの為、それをもとにページのデザインの製作をお願いいたします。
※添付ファイルにてご確認ください。
・依頼するLPは1ページです。
・メインビューの画像の製作をお願いいたします。
※詳細はワイヤーにてご確認ください
・LP内で使用する素材はこちらで用意いたします。
※添付にてご確認ください。
・レスポンシブデザインでお願いします。

◆使用目的
・広告のリンク先としてLPを使用する為、LPを訪れたお客様が
弊社のドライヘッドスパを理解し施術を受けたいと思って
いただくことが目的となります。

◆備考

LPサイトのデザインをご提案いただき依頼者を決定させていただきますので
何卒よろしくお願いいたします。
ご質問等ございましたら遠慮なくご連絡ください。
サイトURL
https://kolune.jp/
ページ数
1ページ
希望イメージ
シンプル 複雑
単色 カラフル
暗い 明るい
日常 高級
遊び心 厳粛
未来的 伝統的
女性的 男性的
希望する色
黄・オレンジ系
すでに沢山のご提案をいただいており、選定に早めに取り掛かるため、
一週間提案の締め切りを前倒しさせていただきますので
ご了承いただけますと幸いでございます。

こちらの要望に最も近く、見やすさとデザイン性が気に入った為、
選ばせていただきました。

この度は弊社の募集にご提案いただきまして誠にありがとうございます。
今後とも機会がございましたら、ご応募いただけますと幸いでございます。

```html
<!DOCTYPE html>
<html lang="ja">
<head>
<meta charset="utf-8">
<title>kolune ドライヘッドスパ</title>
<link href="https://fonts.googleapis.com/css2?family=Noto+Sans+JP:wght@400;500;700&family=Noto+Serif+JP:wght@500;600&family=Playfair+Display:ital@1&display=swap" rel="stylesheet">
<style>
:root{
  --orange:#e8843a;
  --orange-deep:#d9702a;
  --peach:#fcefe4;
  --cream:#fff8f0;
  --blush:#f9e0e0;
  --ink:#4a3f38;
  --muted:#7a6e66;
  --white:#ffffff;
  --photo-warm:#e9ddd2;
  --photo-room:#cdb9a3;
}
*{margin:0;padding:0;box-sizing:border-box}
html,body{width:1200px;height:4280px;overflow:hidden;background:var(--white)}
body{font-family:"Noto Sans JP",sans-serif;color:var(--ink);position:relative}
.abs{position:absolute}
.brand{left:40px;top:28px;font-size:40px;font-weight:700;color:var(--orange);letter-spacing:1px;z-index:2}
.hero{left:0;top:0;width:1200px;height:680px;background:linear-gradient(100deg,#f7f3ef 0%,#efe6dc 45%,#d9c9ba 100%)}
.hero-title{left:112px;top:100px;font-family:"Noto Serif JP",serif;font-size:72px;font-weight:600;color:var(--ink);letter-spacing:6px}
.hero-sub{left:150px;top:205px;font-family:"Noto Serif JP",serif;font-size:34px;color:var(--ink);letter-spacing:4px}
.badge{left:120px;top:400px;width:150px;height:150px;border-radius:50%;background:var(--blush);color:var(--orange);display:flex;flex-direction:column;align-items:center;justify-content:center;font-size:34px;font-weight:700;line-height:1.1}
.badge small{font-size:24px}
.campaign{left:300px;top:410px;color:var(--orange);font-weight:700}
.campaign .label{font-size:38px;display:block;margin-left:20px}
.campaign .price{font-size:66px;display:block;margin-top:4px}
.sec-title{width:1200px;text-align:center;font-size:38px;font-weight:500;color:var(--ink)}
.photo{border-radius:6px}
.about-photo{left:120px;top:790px;width:960px;height:360px;background:linear-gradient(90deg,#efe8e0,#d8c6b5 60%,#efe3d6)}
.price-card{left:790px;top:930px;width:330px;height:230px;background:var(--cream);border:3px solid var(--orange);border-radius:6px;padding:14px 30px}
.price-card h3{font-family:"Playfair Display",serif;font-style:italic;font-weight:400;font-size:40px;color:var(--orange);text-align:center}
.price-row{display:flex;justify-content:space-between;font-size:30px;color:var(--ink);line-height:1.45;border-bottom:1px dashed #e6c7ac}
.lead{width:1200px;text-align:center;font-size:44px;font-weight:700;color:var(--orange)}
.body-text{width:1200px;text-align:center;font-size:22px;line-height:1.75;color:var(--ink)}
.room-a{left:120px;top:1490px;width:480px;height:250px;background:linear-gradient(180deg,#e6ddd3,var(--photo-room))}
.room-b{left:640px;top:1490px;width:440px;height:250px;background:linear-gradient(180deg,#e9e0d6,#c9b29a)}
.btn{width:380px;height:120px;border-radius:60px;background:var(--orange);color:var(--white);display:flex;align-items:center;justify-content:center;gap:28px;font-size:30px;font-weight:500;box-shadow:0 6px 0 var(--orange-deep)}
.btn svg{width:64px;height:64px}
.effects{left:0;top:2220px;width:1200px;height:1220px;background:var(--peach)}
.card{left:100px;width:1000px;background:var(--white);border-radius:8px;box-shadow:0 4px 14px rgba(180,120,70,.15)}
.illust{background:linear-gradient(135deg,#fbeee2,#f3d9bf);border-radius:6px}
.card-text{width:560px}
.card-text h4{font-size:32px;color:var(--orange);font-weight:700;margin-bottom:14px}
.card-text p{font-size:20px;line-height:1.7;color:var(--ink)}
.map{left:120px;top:3570px;width:480px;height:330px;background:linear-gradient(135deg,#eef1f3,#dfe5e9)}
.info{left:650px;top:3560px;font-size:21px;line-height:1.75;color:var(--ink)}
.info h5{font-size:28px;font-weight:700;margin-bottom:10px}
.footer{left:0;top:4200px;width:1200px;height:80px;background:var(--orange);color:var(--white);font-size:24px;display:flex;align-items:center;justify-content:center}
</style>
</head>
<body>

<div class="abs hero" role="img" aria-label="ヘッドスパの施術を受けてくつろぐ女性の写真"></div>
<div class="abs brand">kolune</div>
<h1 class="abs hero-title">ドライヘッドスパ</h1>
<p class="abs hero-sub">気軽に味わえる至福の時間</p>
<div class="abs badge">1/31<small>まで</small></div>
<div class="abs campaign"><span class="label">キャンペーン価格</span><span class="price">40分 2,900円</span></div>

<h2 class="abs sec-title" style="top:712px">koluneドライヘッドスパについて</h2>
<div class="abs photo about-photo" role="img" aria-label="頭皮をほぐす施術風景の写真"></div>
<div class="abs price-card">
  <h3>Price</h3>
  <div class="price-row"><span>25分</span><span>¥2,900</span></div>
  <div class="price-row"><span>40分</span><span>¥4,400</span></div>
  <div class="price-row" style="border:none"><span>55分</span><span>¥5,900</span></div>
</div>
<p class="abs lead" style="top:1170px">小さな幸せ、何度でも</p>
<p class="abs body-text" style="top:1244px">後頭部や側頭部にある筋肉を、オールハンドで心地よくほぐします。<br>短時間でもしっかりと効果が実感でき、ふわふわとした多幸感に包まれ、<br>気づいたらつい眠ってしまうことも。<br>リラックスはもちろんのこと様々な美容効果も<br>期待できるのでぜひご体感ください。</p>

<div class="abs photo room-a" role="img" aria-label="明るい店内の待合スペースの写真"></div>
<div class="abs photo room-b" role="img" aria-label="カーテンで仕切られた施術スペースの写真"></div>
<p class="abs lead" style="top:1762px">オトナ女子向け、お洒落空間</p>
<p class="abs body-text" style="top:1834px">店内は落ち着いた雰囲気のお洒落な空間となっております。<br>施術席に関しても日頃の疲れを忘れられるプライバシーの守られた半個室のため<br>まわりを気にすることなくごゆっくりとお過ごしいただけます。</p>

<div class="abs btn" style="left:180px;top:2060px">
  <svg viewBox="0 0 24 24" fill="none" stroke="#fff" stroke-width="2"><rect x="2" y="4" width="20" height="13" rx="1.5"/><path d="M8 21h8M12 17v4"/></svg>WEBで予約</div>
<div class="abs btn" style="left:660px;top:2060px">
  <svg viewBox="0 0 24 24" fill="#fff"><path d="M6.6 10.8a15.1 15.1 0 0 0 6.6 6.6l2.2-2.2c.3-.3.7-.4 1-.2 1.1.4 2.3.6 3.6.6.6 0 1 .4 1 1V20c0 .6-.4 1-1 1A17 17 0 0 1 3 4c0-.6.4-1 1-1h3.5c.6 0 1 .4 1 1 0 1.3.2 2.5.6 3.6.1.3 0 .7-.2 1z"/></svg>電話で予約</div>

<div class="abs effects"></div>
<h2 class="abs sec-title" style="top:2300px">ドライヘッドスパの効果</h2>

<div class="abs card" style="top:2390px;height:250px">
  <div class="abs illust" style="left:20px;top:20px;width:340px;height:210px" role="img" aria-label="目の疲れに悩む女性のイラスト"></div>
  <div class="abs card-text" style="left:410px;top:22px">
    <h4>眼精疲労の改善</h4>
    <p>長時間のパソコンやスマホの使用による眼精疲労が<br>急増しています。目の周りが緊張し、目のサイクや<br>血流が悪くなり疲れ目につながります。<br>頭をほぐすことで目元まで軽くなり、<br>視界がすっきりする感覚を味わえます。</p>
  </div>
</div>

<div class="abs card" style="top:2670px;height:370px">
  <div class="abs card-text" style="left:40px;top:26px">
    <h4>寝つきの良さ、睡眠の質が向上</h4>
    <p>現代人の5人に1人が「不眠症」と言われています。<br>睡眠が浅くなる原因はストレスや自律神経の乱れ<br>などさまざまです。<br>頭皮をほぐし緊張をゆるめることで、<br>眠りに入りやすい状態へと導きます。<br>施術中に眠ってしまう方も多く、深い休息を<br>実感いただけるのも魅力のひとつです。</p>
  </div>
  <div class="abs illust" style="left:640px;top:40px;width:320px;height:290px" role="img" aria-label="気持ちよく眠る女性のイラスト"></div>
</div>

<div class="abs card" style="top:3080px;height:320px">
  <div class="abs illust" style="left:20px;top:20px;width:340px;height:280px" role="img" aria-label="首と肩のこりに悩む女性のイラスト"></div>
  <div class="abs card-text" style="left:410px;top:26px">
    <h4>首・肩こりの軽減</h4>
    <p>頭皮と首まわりは筋肉でつながっており、<br>頭をほぐすと首や肩までゆるみます。<br>デスクワークで固まった筋肉の緊張がとけ、<br>血の巡りがよくなることで重さが軽減します。<br>定期的に受けることでより効果が続きます。</p>
  </div>
</div>

<h2 class="abs sec-title" style="top:3488px">アクセス</h2>
<div class="abs photo map" role="img" aria-label="店舗周辺の地図"></div>
<div class="abs info">
  <h5>ネイル&amp;ドライヘッドスパ kolune</h5>
  東京都台東区花見町 2-8-11<br>緑風ビル B1F<br>TEL:03-4521-7390<br>営業時間 平日 13:00 ～ 22:00<br>　　土日・祝日 13:00 ～ 22:00<br>クレジット 主要クレジットカード<br>電子マネー対応
</div>

<div class="abs btn" style="left:180px;top:4030px">
  <svg viewBox="0 0 24 24" fill="none" stroke="#fff" stroke-width="2"><rect x="2" y="4" width="20" height="13" rx="1.5"/><path d="M8 21h8M12 17v4"/></svg>WEBで予約</div>
<div class="abs btn" style="left:660px;top:4030px">
  <svg viewBox="0 0 24 24" fill="#fff"><path d="M6.6 10.8a15.1 15.1 0 0 0 6.6 6.6l2.2-2.2c.3-.3.7-.4 1-.2 1.1.4 2.3.6 3.6.6.6 0 1 .4 1 1V20c0 .6-.4 1-1 1A17 17 0 0 1 3 4c0-.6.4-1 1-1h3.5c.6 0 1 .4 1 1 0 1.3.2 2.5.6 3.6.1.3 0 .7-.2 1z"/></svg>電話で予約</div>

<footer class="abs footer">© Copyright 2021 kolune. All rights reserved.</footer>
</body>
</html>
```